Vantrel Web Services

This is a new It services company operating in Perth western Australia

we need a website that is easy to navigate without a cluttered feel to it it should have the following links and pages

About Us
Services
Clients
Contact Us
MY Vantrel (login for clients)

Hi it is a web based IT services company so we would expect customers to come to the website for 2 different purposes the first is to enquire about our services and then as they become customers come to our website to manage their services so whilst they are seperate we want do not want it to look like 2 different websites

hope this helps

Hi to update this we need a home page and templates for sub pages

this is a design brief only and not the coding of the pages or building of the site

```html
<!DOCTYPE html>
<html lang="en">
<head>
<meta charset="utf-8">
<title>Vantrel Web Services</title>
<link href="https://fonts.googleapis.com/css2?family=Source+Sans+Pro:ital,wght@0,400;0,600;0,700;1,400&family=Questrial&display=swap" rel="stylesheet">
<style>
:root{
  --red:#c41a1f;
  --red-dark:#8e0a0d;
  --red-deep:#a30b0f;
  --blue:#1d3c9c;
  --ink:#2b2b2b;
  --muted:#8a93a3;
  --soft:#f6f7f8;
  --line:#dfe2e6;
  --footer:#f0f0f0;
  --bar:#4a4a4a;
}
*{margin:0;padding:0;box-sizing:border-box}
html,body{width:996px;height:1200px;overflow:hidden}
body{position:relative;background:#fcfcfc;font-family:"Source Sans Pro",sans-serif;color:var(--ink)}
.abs{position:absolute}
/* header */
.header{left:0;top:0;width:996px;height:77px;background:linear-gradient(#f7f7f7,#e3e3e3)}
.brand{left:132px;top:9px;display:flex;align-items:center;gap:8px}
.brand-dot{width:30px;height:30px;border-radius:50%;background:var(--red)}
.brand-name{font-size:24px;font-weight:700;color:var(--blue);letter-spacing:1px}
.phone{left:630px;top:16px;font-size:14px;font-weight:600;color:#555;display:flex;gap:6px;align-items:center}
.login{left:759px;top:9px;width:101px;height:31px;border-radius:16px;background:#fff;border:1px solid #d3d3d3;box-shadow:0 1px 2px rgba(0,0,0,.15);display:flex;align-items:center;justify-content:center;gap:6px;font-size:11.5px;font-weight:600;color:#555}
.login i{width:16px;height:16px;border-radius:50%;background:var(--red)}
.nav{left:132px;top:54px;width:732px;height:39px;background:linear-gradient(#fff,#ececec);border:1px solid #d7d7d7;border-radius:3px;z-index:3;display:flex;padding-left:18px}
.nav a{font-size:10.5px;font-weight:700;color:#444;text-decoration:none;line-height:38px;padding:0 18px}
.nav a.active{color:var(--red-dark);background:#e8e8e8}
/* hero */
.hero{left:0;top:77px;width:996px;height:375px;background:radial-gradient(ellipse at 55% 80%,#f06066 0%,#d82a31 45%,#b10f15 75%,#7d0507 100%);overflow:hidden}
.hero-person{left:210px;top:38px;width:250px;height:337px;border-radius:110px 110px 0 0;background:linear-gradient(#3b3d45,#15161b)}
.hero-kicker{left:514px;top:108px;font-size:31px;font-weight:700;color:#f4b6b8;letter-spacing:.5px}
.hero-title{left:513px;top:138px;font-size:48px;font-weight:700;color:#fff;letter-spacing:3px}
.hero-text{left:519px;top:203px;width:300px;font-size:15px;line-height:20px;color:#fff}
.btn-blue{left:518px;top:266px;width:109px;height:35px;background:linear-gradient(#2d56c8,#173996);border:1px solid #10286e;border-radius:2px;color:#fff;font-size:10.5px;font-weight:700;display:flex;align-items:center;justify-content:center}
/* features */
.card{top:504px;width:234px;height:171px;background:var(--soft);border:1px solid #e4e6e9;text-align:center}
.card-icon{top:-31px;left:92px;width:56px;height:56px;border-radius:8px;background:var(--red-dark);display:flex;align-items:center;justify-content:center}
.card h3{margin-top:44px;font-size:13px;font-weight:700;letter-spacing:.3px}
.card p{margin-top:7px;font-size:10.5px;line-height:15.5px;color:var(--muted)}
.btn-red{display:inline-block;margin-top:12px;width:70px;height:23px;line-height:23px;background:linear-gradient(#c42a2e,#9b0f13);color:#fff;font-size:9px;font-weight:600;border-radius:2px}
/* testimonial + news */
.section-title{font-size:14px;font-weight:700;letter-spacing:.2px}
.avatar{left:139px;top:752px;width:62px;height:62px;border-radius:50%;background:linear-gradient(#6a4a3a,#c99a85)}
.person{left:120px;top:831px;width:100px;text-align:center}
.person b{display:block;font-size:12px;color:#555}
.person span{font-size:9.5px;color:#666}
.quote{left:231px;top:750px;width:382px;height:110px;background:var(--soft);border:1px solid #d6d9dd;padding:14px 22px;font-style:italic;font-size:12px;line-height:18.6px;color:#777}
.quote:before{content:"";position:absolute;left:-8px;top:28px;width:14px;height:14px;background:var(--soft);border-left:1px solid #d6d9dd;border-bottom:1px solid #d6d9dd;transform:rotate(45deg)}
.news{left:633px;width:230px;display:flex;gap:11px}
.news .thumb{width:42px;height:42px;flex:none;background:linear-gradient(135deg,#4a5663,#a9b3bd)}
.news p{font-size:9.5px;line-height:15.5px;color:var(--muted)}
.news p b{font-weight:400;color:#555}
/* clients */
.clients{left:0;top:899px;width:996px;height:88px;background:radial-gradient(ellipse at 40% 50%,#b2373d,#9e0c10 60%,#a50c0f)}
.clients-title{left:134px;top:934px;font-size:13.5px;font-weight:700;color:#fff}
.client{top:930px;font-size:20px;font-weight:700;color:#fff;display:flex;align-items:center;gap:6px}
.client i{width:12px;height:12px;border-radius:50%;background:#fff}
/* footer */
.footer{left:0;top:987px;width:996px;height:174px;background:var(--footer)}
.foot-h{top:1024px;font-family:"Questrial",sans-serif;font-size:11px;font-weight:700;letter-spacing:1px;color:#444;text-transform:uppercase}
.foot-about{left:130px;top:1075px;width:180px;font-size:9.5px;line-height:15.5px;color:var(--muted)}
.foot-nav{left:386px;top:1050px;list-style:none}
.foot-nav li{font-size:9.5px;color:#666;height:23.2px;padding-left:12px;position:relative}
.foot-nav li:before{content:"";position:absolute;left:0;top:3px;border-left:4px solid #555;border-top:3.5px solid transparent;border-bottom:3.5px solid transparent}
.social{left:513px;top:1051px;display:flex;gap:13px}
.social span{width:25px;height:25px;background:var(--red-dark)}
.contact{left:697px;top:1050px;font-size:9.5px;color:#666}
.contact div{display:flex;gap:10px;height:23.2px}
.contact svg{width:14px;height:14px;flex:none}
.bottom{left:0;top:1161px;width:996px;height:39px;background:var(--bar);color:#fff;font-size:9.5px;font-weight:600;line-height:39px}
</style>
</head>
<body>
<header class="abs header"></header>
<div class="abs brand"><span class="brand-dot"></span><span class="brand-name">Vantrel</span></div>
<div class="abs phone">
  <svg width="16" height="16" viewBox="0 0 24 24"><path fill="#666" d="M6.6 10.8a15 15 0 006.6 6.6l2.2-2.2c.3-.3.7-.4 1-.2 1.1.4 2.3.6 3.6.6.6 0 1 .4 1 1V20c0 .6-.4 1-1 1A17 17 0 013 4c0-.6.4-1 1-1h3.5c.6 0 1 .4 1 1 0 1.3.2 2.5.6 3.6.1.3 0 .7-.2 1z"/></svg>
  +1800-55-0142
</div>
<div class="abs login"><i></i>MY Vantrel</div>
<nav class="abs nav">
  <a class="active" href="#">HOME</a><a href="#">ABOUT US</a><a href="#">SERVICES</a><a href="#">CLIENTS</a><a href="#">CONTACT US</a>
</nav>

<section class="abs hero">
  <div class="abs hero-person" role="img" aria-label="Photo of a smiling businessman in a dark suit with arms crossed"></div>
  <div class="abs hero-kicker">TRUSTED IN PERTH</div>
  <div class="abs hero-title">IT SERVICES</div>
  <p class="abs hero-text">Lorem ipsum dolor sit amet, consectetur adipisicing elit, sed do eiusmod tempor.</p>
  <div class="abs btn-blue">CONTACT US</div>
</section>

<div class="abs card" style="left:130px">
  <div class="abs card-icon"><svg width="36" height="36" viewBox="0 0 36 36"><circle cx="18" cy="18" r="14" fill="none" stroke="#fff" stroke-width="4"/><circle cx="18" cy="18" r="6" fill="none" stroke="#fff" stroke-width="3"/><path d="M18 4v8M18 24v8M4 18h8M24 18h8" stroke="#fff" stroke-width="5"/></svg></div>
  <h3>IT SUPPORT</h3>
  <p>Fusce gravida tortor felis<br>Ac dictum risus sagittis id morbi posu<br>justo eleifend libero ultricies</p>
  <span class="btn-red">read more</span>
</div>
<div class="abs card" style="left:381px">
  <div class="abs card-icon"><svg width="34" height="30" viewBox="0 0 34 30"><path d="M12 6V3h10v3" fill="none" stroke="#fff" stroke-width="3"/><rect x="2" y="7" width="30" height="21" rx="3" fill="#fff"/><path d="M9 7v21M25 7v21" stroke="#8e0a0d" stroke-width="2"/></svg></div>
  <h3>IT SERVICES</h3>
  <p>Fusce gravida tortor felis<br>Ac dictum risus sagittis id morbi posu<br>justo eleifend libero ultricies</p>
  <span class="btn-red">read more</span>
</div>
<div class="abs card" style="left:628px">
  <div class="abs card-icon"><svg width="24" height="36" viewBox="0 0 24 36"><path d="M12 2a10 10 0 00-6 18v5h12v-5A10 10 0 0012 2z" fill="#fff"/><rect x="7" y="27" width="10" height="3" fill="#fff"/><rect x="9" y="31" width="6" height="3" rx="1" fill="#fff"/><circle cx="12" cy="11" r="3" fill="#8e0a0d"/><rect x="11" y="13" width="2" height="10" fill="#8e0a0d"/></svg></div>
  <h3>IT SOLUTIONS</h3>
  <p>Fusce gravida tortor felis<br>Ac dictum risus sagittis id morbi posu<br>justo eleifend libero ultricies</p>
  <span class="btn-red">read more</span>
</div>

<h2 class="abs section-title" style="left:134px;top:716px">CLIENT TESTIMONIAL</h2>
<div class="abs avatar" role="img" aria-label="Portrait photo of the client"></div>
<div class="abs person"><b>Mara Quill</b><span>Managing Director</span></div>
<blockquote class="abs quote">“Vestibulum blandit faucibus urna in hendrerit. Vivamus leo dui, bibendum vitae hendrerit ac, volutpat quis dolor. Maecenas id lacinia odio, et malesuada lectus. Nulla et ante non metus consec-tetur vestibulum sed quis dolor.”</blockquote>

<h2 class="abs section-title" style="left:632px;top:716px">RECENT NEWS</h2>
<div class="abs news" style="top:750px"><div class="thumb" role="img" aria-label="Photo of colleagues at a laptop"></div><p>Fusce gravida tortor felis, ac dictum risus sagittiso eiusmod tempor incididunt ut<br><b>October 15, 2013</b></p></div>
<div class="abs news" style="top:811px"><div class="thumb" role="img" aria-label="Photo of hands using a tablet"></div><p>Fusce gravida tortor felis, ac dictum risus sagittiso eiusmod tempor incididunt ut<br><b>October 15, 2013</b></p></div>

<section class="abs clients"></section>
<div class="abs clients-title">OUR CLIENTS</div>
<div class="abs client" style="left:284px"><i></i>Hueline</div>
<div class="abs client" style="left:398px">Brightcast</div>
<div class="abs client" style="left:535px">Kestrel OS</div>
<div class="abs client" style="left:668px"><i></i>Gemstay</div>
<div class="abs client" style="left:790px">Tidepool</div>

<footer class="abs footer"></footer>
<div class="abs brand" style="top:1020px"><span class="brand-dot"></span><span class="brand-name">Vantrel</span></div>
<p class="abs foot-about">Donec volutpat, mi vel egestas eleifend, dolor arcu iaculis nunc. Fusce gravida tortor felis, ac dictum risus sagittis id.</p>
<h4 class="abs foot-h" style="left:385px">Navigation</h4>
<ul class="abs foot-nav"><li>Home</li><li>About Vantrel</li><li>Our Services</li><li>Clients</li></ul>
<h4 class="abs foot-h" style="left:511px">Social</h4>
<div class="abs social" aria-label="Social links"><span></span><span></span><span></span><span></span></div>
<h4 class="abs foot-h" style="left:697px">Contact Details</h4>
<div class="abs contact">
  <div><svg viewBox="0 0 24 24"><path fill="#777" d="M6.6 10.8a15 15 0 006.6 6.6l2.2-2.2c.3-.3.7-.4 1-.2 1.1.4 2.3.6 3.6.6.6 0 1 .4 1 1V20c0 .6-.4 1-1 1A17 17 0 013 4c0-.6.4-1 1-1h3.5c.6 0 1 .4 1 1 0 1.3.2 2.5.6 3.6.1.3 0 .7-.2 1z"/></svg>+1800-555-0199</div>
  <div><svg viewBox="0 0 24 24"><rect x="3" y="5" width="18" height="14" rx="1" fill="none" stroke="#777" stroke-width="2"/><path d="M3 6l9 7 9-7" fill="none" stroke="#777" stroke-width="2"/></svg>info@vantrelweb.com</div>
  <div><svg viewBox="0 0 24 24"><path fill="#777" d="M12 2a7 7 0 00-7 7c0 5 7 13 7 13s7-8 7-13a7 7 0 00-7-7zm0 9.5A2.5 2.5 0 1112 6.5a2.5 2.5 0 010 5z"/></svg><span>Your Address, Your Country<br>Your Zip Code</span></div>
</div>
<div class="abs bottom"><span style="position:absolute;left:130px">Copyright © 2014 - Vantrel. All Rights reserved</span><span style="position:absolute;left:700px">Privacy Policy</span><span style="position:absolute;left:787px">Sitemap</span></div>
</body>
</html>
```